Flyer-Design für Verlegung von fugenlosen Böden
Zielgruppe
Die Firma KORVAL, hat seinen Hauptaugenmerk auf das verlegen von fugenlosen Böden gelegt.
welchen Vorteil bietet Ihnen dieser Bodenbelag? Der fugenlose Bodenbelag wie der Epoxidharzboden oder der Steinteppich ist in den letzten Jahren eine beliebte Alternative zu Laminat, Fliesen, Parkett und anderen Bodenbelägen geworden.Seine steigende Beliebtheit verdankt der fugenlose Bodenbelag unter anderem seiner Robustheit.Unsere Bodenbeläge sind Geruchsneutral und bietet eine lange Lebensdauer. Die Zielgruppe sind Private sowie Gewerbliche Kunden.
Aufgabenstellung
Der Text sollte den effekt, 'Wow' das muss ich haben beim Leser auslösen. Das gleiche zählt für die verwendeten Bilder die der Desinger gerne auswählen derf. Mehr Infos Z.b Logo kann sich der Desinger auf der Webseite entnehmen.
www.korval-estrich.example

```html
<!DOCTYPE html>
<html lang="de">
<head>
<meta charset="utf-8">
<title>KORVAL – Fugenlose Bodenbeläge</title>
<link rel="stylesheet" href="https://fonts.googleapis.com/css2?family=Source+Sans+3:wght@400;600&display=swap">
<style>
  :root {
    --accent: #c64a0a;
    --text: #40464a;
    --paper: #ffffff;
    --on-accent: #ffffff;
  }
  * { margin: 0; padding: 0; box-sizing: border-box; }
  html, body { width: 1200px; height: 846px; overflow: hidden; background: var(--paper); }
  .flyer {
    position: relative;
    width: 1200px;
    height: 846px;
    background: var(--paper);
    font-family: "Source Sans 3", sans-serif;
    color: var(--text);
  }
  .headline {
    position: absolute;
    left: 57px;
    top: 50px;
    font-size: 26.5px;
    font-weight: 600;
    color: var(--accent);
    white-space: nowrap;
  }
  .intro {
    position: absolute;
    left: 57px;
    font-size: 21.5px;
    line-height: 29px;
    white-space: nowrap;
  }
  .intro--first { top: 112px; }
  .intro--second { top: 345px; }
  .brand {
    position: absolute;
    left: 60px;
    top: 594px;
    display: flex;
    align-items: center;
    gap: 14px;
  }
  .brand__mark {
    width: 22px;
    height: 22px;
    background: var(--accent);
  }
  .brand__name {
    font-size: 64px;
    font-weight: 600;
    line-height: 1;
    letter-spacing: 3px;
    color: var(--text);
  }
  .contact {
    position: absolute;
    left: 68px;
    top: 713px;
    font-size: 21.5px;
    line-height: 29px;
    white-space: nowrap;
  }
  .benefits {
    position: absolute;
    left: 832px;
    top: 0;
    width: 368px;
    height: 846px;
    background: var(--accent);
    color: var(--on-accent);
    list-style: none;
  }
  .benefit {
    position: absolute;
    left: 30px;
    display: flex;
    align-items: center;
    gap: 18px;
    font-size: 23px;
    line-height: 29px;
    white-space: nowrap;
  }
  .benefit svg { flex: none; width: 46px; height: 40px; }
</style>
</head>
<body>
<main class="flyer">
  <h1 class="headline">Warum ein fugenloser Boden?</h1>

  <p class="intro intro--first">
    Je mehr unterschiedliche Materialien als Fußbodenbelag eingesetzt<br>
    werden, desto kleiner und unruhiger wirkt das gesamte Interieur.<br>
    Der durchgehende, fugenlose Boden hingegen hält sich elegant im Hin-<br>
    tergrund und schafft eine ruhige Atmosphäre. Keine ablenkenden Muster<br>
    oder Absätze stören das Bild, wodurch kleine Räume größer wirken.<br>
    Besonders toll kommt das auch in offenen Küchen mit anschließendem<br>
    Wohn-Ess-Bereich zur Geltung.
  </p>

  <p class="intro intro--second">
    Einer der wichtigsten Vorteile gegenüber vielen anderen Bodenbelägen<br>
    ist, dass der fugenlose Boden besonders robust und leicht zu pflegen ist.<br>
    Er wird mit mehreren Schichten versiegelt und hat keine störenden Fugen.<br>
    Anders als bei Parkett, Laminat ,Fliesen oder Vinyl ist er unempfindlich<br>
    gegen Kratzer und Stöße.
  </p>

  <div class="brand">
    <span class="brand__mark"></span>
    <span class="brand__name">KORVAL</span>
  </div>

  <address class="contact" style="font-style: normal;">
    Lindenhang 12 &nbsp;|&nbsp; 66999 Talbrück<br>
    Tel.: 06800-5550123 | Mobil: 0170 - 55 50 19 8<br>
    email: fugenlos@korval-estrich.example &nbsp;|&nbsp; fugenlos-korval.example
  </address>

  <svg width="0" height="0" style="position:absolute">
    <defs>
      <symbol id="tick" viewBox="0 0 46 40">
        <path d="M34 8 A18 18 0 1 0 38 22" fill="none" stroke="#fff" stroke-width="3.4" stroke-linecap="round"/>
        <path d="M11 19 L19 28 L44 3" fill="none" stroke="#fff" stroke-width="4.4" stroke-linecap="round" stroke-linejoin="round"/>
      </symbol>
    </defs>
  </svg>

  <ul class="benefits">
    <li class="benefit" style="top:86px"><svg><use href="#tick"/></svg><span>Dem Design sind keine<br>Grenzen gesetzt</span></li>
    <li class="benefit" style="top:174px"><svg><use href="#tick"/></svg><span>Freie Farbauswahl aus<br>über 200 Farben<br>(metallic,matt)</span></li>
    <li class="benefit" style="top:290px"><svg><use href="#tick"/></svg><span>Ihr Persönliches<br>Einzelstück</span></li>
    <li class="benefit" style="top:376px"><svg><use href="#tick"/></svg><span>Weil Ihr Boden kein<br>Standart Boden<br>werden soll!</span></li>
    <li class="benefit" style="top:493px"><svg><use href="#tick"/></svg><span>Der Boden mit dem<br>Wow Effekt!</span></li>
    <li class="benefit" style="top:580px"><svg><use href="#tick"/></svg><span>Geben Sie sich nicht<br>mit weniger zufrieden!</span></li>
    <li class="benefit" style="top:667px"><svg><use href="#tick"/></svg><span>Hochglanz &nbsp;oder Matt<br>Versiegelung</span></li>
  </ul>
</main>
</body>
</html>
```